Petal Sprite - web design for my new flower atelier

I would like to ask for design proposal for my newly established flower atelier. My brand name is Petal Sprite and I focus on realisation of events and flower projects (any kind) for physical as well as legel persons. I don’t operate as a standard flowershop. I would like to have 5 key parts - 1/Landing pg/welcome, 2/About me, 3/Gallery, 4/References, 5/Contact details. I would like the web design to reflect the way I am/ I do the things, ie, be slightly different, do non-tradiotional arrangements, my passion for flowers, gentle& fregile style, love for minimalism and details in the arrangements. I attach couple of photos of what I do so that you can better understand my style . You can see more on IG mirka_petal_sprite or FB Petal Sprite. I was wondering maybe one of the first 2 photos could be part of the landing pg. Or another idea is to have a design similar to this one https://thistlebloomstudio.example, ie to choose 3-5photos which are being animated like here. However, I am open to discuss any ideas and look forward for all the proposals.

Target Market(s)

physical as well as legal persons - weddings, celebrations, business events, projects for hotels, beaty salons, restaurants and others.. actually any kind of flower project

Industry/Entity Type

flowers

Number of Pages Required

1 page

Font styles to use
Other font styles liked:
• the font which matches the logo font style

Requirements
Must have
• to reflect the way I am as described above, I prefer more simple way of design, with the attention to a detail, I prefer pastel colours

```html
<!DOCTYPE html>
<html lang="en">
<head>
<meta charset="utf-8">
<title>Petal Sprite – Flower Atelier</title>
<link href="https://fonts.googleapis.com/css2?family=Questrial&display=swap" rel="stylesheet">
<style>
:root{
  --ink:#111;
  --brown:#3f2e1f;
  --logo:#7a5a3a;
  --gold:#9a6420;
  --muted:#8a8a8a;
  --grey-dot:#7b7b7b;
  --page:#fafafa;
  --band:#f7f7f7;
  --block:#efefef;
  --white:#fff;
  --line:#555;
  --wood:#8a6a4e;
  --leaf-deep:#7f9f55;
  --leaf-mid:#a8c474;
  --leaf-light:#d2e2a8;
  --mist:#dfe6da;
}
*{margin:0;padding:0;box-sizing:border-box}
html,body{width:1200px;height:3524px;overflow:hidden}
body{position:relative;background:var(--page);font-family:'Questrial',sans-serif;color:var(--ink)}
.abs{position:absolute}

/* hero */
.hero-photo{left:0;top:0;width:1200px;height:810px;
  background:
    radial-gradient(circle at 28% 48%,rgba(244,240,190,.75) 0,rgba(244,240,190,0) 12%),
    radial-gradient(circle at 60% 86%,rgba(230,214,236,.7) 0,rgba(230,214,236,0) 10%),
    radial-gradient(ellipse at 80% 40%,var(--leaf-light) 0,rgba(210,226,168,0) 35%),
    radial-gradient(ellipse at 12% 70%,var(--leaf-mid) 0,rgba(168,196,116,0) 40%),
    linear-gradient(90deg,var(--wood) 0%,var(--leaf-deep) 22%,var(--leaf-mid) 50%,var(--leaf-deep) 78%,var(--mist) 100%)}
.hero-card{left:372px;top:178px;width:457px;height:454px;background:var(--white)}
.hero-frame{left:391px;top:196px;width:417px;height:417px;border:1px solid var(--brown)}
.brand-mark{left:391px;width:417px;top:376px;text-align:center;font-size:42px;color:var(--logo);line-height:1}
.hero-title{left:391px;width:417px;top:458px;text-align:center;font-size:38px;line-height:44px;color:var(--brown)}
.hero-scroll{left:391px;width:417px;top:566px;text-align:center;font-size:18px;color:var(--gold)}

/* nav */
.nav{top:838px;left:0;width:1200px;height:24px}
.nav a{position:absolute;font-size:18px;color:#222;text-decoration:none;transform:translateX(-50%);white-space:nowrap}
.nav-dot{left:416px;top:872px;width:4px;height:4px;border-radius:50%;background:#222}
.leaf{left:1005px;top:810px;width:195px;height:209px;border-radius:60% 0 0 70%;
  background:linear-gradient(200deg,#3f7a36,#2a5a26)}

/* about */
.about-block{left:0;top:947px;width:376px;height:243px;background:var(--block)}
.about-photo{left:98px;top:992px;width:416px;height:416px;
  background:linear-gradient(135deg,#c9ccd6 0%,#b3adba 45%,#dcc6ac 70%,#9aa0ae 100%)}
.about-title{left:599px;top:990px;font-size:55px;line-height:60px;font-weight:normal}
.about-rule{left:575px;top:1166px;width:1px;height:242px;background:var(--ink)}
.about-text{left:599px;top:1164px;width:505px;font-size:13.5px;line-height:16.5px}
.about-text p{margin-bottom:16px}

/* gallery */
.gallery{left:0;top:1491px;width:1200px;height:835px;background:var(--white)}
.gallery-ghost{left:71px;top:1530px;font-size:100px;color:#f2f2f2;line-height:1;white-space:nowrap}
.gallery-title{left:98px;top:1584px;font-size:64px;line-height:1;font-weight:normal}
.gallery-intro{left:98px;top:2193px;width:330px;font-size:13.5px;line-height:16.5px}
.work-img{width:293px}
.work-season{font-size:18px;font-weight:bold;width:293px}
.work-desc{font-size:22px;line-height:26px;color:var(--muted);width:300px}
.tone-a{background:linear-gradient(180deg,#7a8a5e,#b4aea6 60%,#7a5a42)}
.tone-b{background:linear-gradient(180deg,#c89072,#8a3a28)}
.tone-c{background:linear-gradient(180deg,#f2f2f0,#5a7a44 40%,#333 80%,#eee)}
.tone-d{background:linear-gradient(160deg,#a4a49c,#cdc97a 40%,#c49ad0 65%,#96968e)}
.tone-e{background:linear-gradient(180deg,#34405a,#9498a0,#44444a)}

/* references */
.refs{left:0;top:2326px;width:1200px;height:472px;background:var(--band);overflow:hidden}
.refs-title{left:100px;top:2422px;font-size:64px;line-height:1;font-weight:normal}
.ref{width:270px}
.ref-num{width:60px;height:60px;border-radius:50%;background:var(--grey-dot);color:#fff;font-size:26px;line-height:60px;text-align:center}
.ref-name{margin-top:10px;font-size:23px;color:var(--muted)}
.ref-pos{margin-top:6px;font-size:19px;color:#444}
.ref-text{margin-top:38px;font-size:13px;line-height:16.5px;color:var(--muted);width:200px}
.refs-rule{left:0;top:2761px;width:551px;height:1px;background:#999}

/* contact */
.contact-title{left:100px;top:2948px;font-size:66px;line-height:1;font-weight:normal}
.contact-mail{left:784px;top:2988px;font-size:15px}
.say-hello{left:104px;top:3102px;font-size:38px;line-height:1}
.field{font-size:24px;line-height:1}
.field-line{height:1px;background:var(--line)}
.submit{left:101px;top:3368px;width:207px;height:53px;border:1px solid #222;background:transparent;font-family:inherit;font-size:23px;color:var(--ink)}
.find-us{left:784px;top:3303px;font-size:18px}
.social{width:34px;height:34px;border-radius:50%;background:#222}
.address{left:952px;top:3303px;font-size:18px;font-weight:bold}
.phone{left:952px;top:3342px;font-size:18px;color:#aaa}
</style>
</head>
<body>

<!-- hero -->
<div class="abs hero-photo" role="img" aria-label="Lush arrangement of green foliage and pale spring flowers against a wooden wall"></div>
<div class="abs hero-card"></div>
<div class="abs hero-frame"></div>
<div class="abs brand-mark">Petal Sprite</div>
<div class="abs hero-title">Fresh flowers<br>Everyday</div>
<div class="abs hero-scroll">Scroll to see more</div>

<!-- navigation -->
<nav class="abs nav">
  <a style="left:286px">Home</a>
  <a style="left:418px">About me</a>
  <a style="left:553px">Gallery</a>
  <a style="left:695px">References</a>
  <a style="left:873px">Contact details</a>
</nav>
<div class="abs nav-dot"></div>
<div class="abs leaf" role="img" aria-label="Large tropical monstera leaf"></div>

<!-- about -->
<div class="abs about-block"></div>
<div class="abs about-photo" role="img" aria-label="Florist in a winter scarf holding a wrapped bouquet outdoors"></div>
<h2 class="abs about-title">About<br>Me</h2>
<div class="abs about-rule"></div>
<div class="abs about-text">
  <p>Founded in 2009, Petal Sprite's owner, Maren, started the business to offer an eco-friendly option for couples planning their weddings. While most Petal Sprite's work is wedding-focused, we also offer floral design for corporate and social events.</p>
  <p>At Petal Sprite, environmental and social responsibility take center stage. With our eco-conscious approach, we seek out the best flowers of each season.</p>
  <p>Our eco-friendly practices include:<br>• working with local flower farmers as much as possible<br>• composting our unused leaves, stems, etc.<br>• eliminating toxic floral foam from our studio<br>• donating the flowers returned from our events through Second Bloom, our flower donation program.</p>
</div>

<!-- gallery -->
<section class="abs gallery"></section>
<div class="abs gallery-ghost">My Work</div>
<h2 class="abs gallery-title">Gallery</h2>
<p class="abs gallery-intro">Petal Sprite offers nature-inspired floral design for weddings and events.<br>With an eco-conscious approach, we seek out the best flowers of each season, embracing garden-style floral design with a touch of whimsy.</p>

<div class="abs work-img tone-a" style="left:561px;top:1493px;height:162px" role="img" aria-label="Spring bouquet in a white ribbed vase on a wooden table"></div>
<div class="abs work-season" style="left:562px;top:1676px">Spring</div>
<div class="abs work-desc" style="left:561px;top:1718px">Spring hand-tied bouquet made with the finest flowers</div>

<div class="abs work-img tone-c" style="left:561px;top:1811px;height:346px" role="img" aria-label="Green foliage arrangement in a dark vase standing in snow"></div>
<div class="abs work-season" style="left:562px;top:2207px">Spring</div>
<div class="abs work-desc" style="left:561px;top:2248px">Spring hand-tied bouquet made with the finest flowers</div>

<div class="abs work-img tone-b" style="left:881px;top:1493px;height:46px" role="img" aria-label="Warm-toned floral detail"></div>
<div class="abs work-season" style="left:882px;top:1559px">Spring</div>
<div class="abs work-desc" style="left:881px;top:1601px">Spring hand-tied bouquet made with the finest flowers</div>

<div class="abs work-img tone-d" style="left:881px;top:1703px;height:348px" role="img" aria-label="Colourful hand-tied bouquet with roses and yellow blooms on wooden boards"></div>
<div class="abs work-season" style="left:882px;top:2071px">Spring</div>
<div class="abs work-desc" style="left:881px;top:2113px">Spring hand-tied bouquet made with the finest flowers</div>

<div class="abs work-img tone-e" style="left:881px;top:2216px;height:82px" role="img" aria-label="Glass vase on a dark stone surface"></div>

<!-- references -->
<section class="abs refs">
  <div class="abs ref" style="left:551px;top:101px">
    <div class="ref-num">1</div>
    <div class="ref-name">Reference Name</div>
    <div class="ref-pos">Position</div>
    <div class="ref-text">Lorem Ipsum Dolor Sit Amet, Consectetur Adipis Elit. Quis Lectus Ipsum Rhon Fermentum Varius Quis.</div>
  </div>
  <div class="abs ref" style="left:832px;top:101px">
    <div class="ref-num">2</div>
    <div class="ref-name">Reference Name</div>
    <div class="ref-pos">Position</div>
    <div class="ref-text">Lorem Ipsum Dolor Sit Amet, Consectetur Adipis Elit. Quis Lectus Ipsum Rhon Fermentum Varius Quis.</div>
  </div>
  <div class="abs ref" style="left:1113px;top:101px">
    <div class="ref-num">3</div>
    <div class="ref-name">Reference Name</div>
    <div class="ref-pos">Position</div>
    <div class="ref-text">Lorem Ipsum Dolor Sit Amet, Consectetur Adipis Elit. Quis Lectus Ipsum Rhon Fermentum Varius Quis.</div>
  </div>
</section>
<h2 class="abs refs-title">References</h2>
<div class="abs refs-rule"></div>

<!-- contact -->
<h2 class="abs contact-title">Let’s get in touch.</h2>
<div class="abs contact-mail">hello@petalsprite.example</div>
<div class="abs say-hello">Say hello</div>
<div class="abs field" style="left:104px;top:3184px">Full Name</div>
<div class="abs field-line" style="left:101px;top:3228px;width:238px"></div>
<div class="abs field" style="left:379px;top:3184px">Email address</div>
<div class="abs field-line" style="left:376px;top:3228px;width:237px"></div>
<div class="abs field" style="left:104px;top:3268px">Message</div>
<div class="abs field-line" style="left:101px;top:3312px;width:513px"></div>
<button class="abs submit">Submit</button>

<div class="abs find-us">Find us</div>
<div class="abs social" style="left:785px;top:3339px" aria-label="Social link"></div>
<div class="abs social" style="left:827px;top:3339px" aria-label="Social link"></div>
<div class="abs social" style="left:785px;top:3387px" aria-label="Social link"></div>
<div class="abs social" style="left:827px;top:3387px" aria-label="Social link"></div>
<div class="abs address">12 Fernside Lane, Larkford</div>
<div class="abs phone">070 5512 0847</div>

</body>
</html>
```